Fernwick Lottery Review and Forecast

Add to features - No Software to Download.
Updates

Some designers have asked for a little extra time. Please extend the deadline.

Target Market(s)

Lottery Players. Not bingo or casino related...please.

Industry/Entity Type

Lottery

Number of Pages Required

5+ page

Requirements
Must have
• Crisp look and Feel. Use lottery related images, not bingo or casino related. Sites for some inspiration – https://www.drawquillo.com/ https://plinthora.com/numbers/ https://www.vornaxel.net/how-to-win-the-lottery https://www.kelbrisa.com/
Nice to have
• See the attached word doc. Here is a site with a feel or similarity of what we want the "Latest Draws page to look like https://www.drawquillo.com/tressin-draw

```html
<!DOCTYPE html>
<html lang="en">
<head>
<meta charset="utf-8">
<title>Fernwick Lottery Software</title>
<link rel="stylesheet" href="https://fonts.googleapis.com/css2?family=Barlow:wght@500;600;700&family=Work+Sans:wght@400;500;600&display=swap">
<style>
:root{
  --red:#f03a2b;
  --ink:#111;
  --text:#555;
  --grey-bg:#f5f5f7;
  --orange:#f0920a;
  --mint:#e6eee7;
  --white:#fff;
  --line:#cfd6d0;
}
*{box-sizing:border-box;margin:0;padding:0}
html,body{width:1200px;height:3339px;overflow:hidden}
body{position:relative;font-family:"Work Sans",sans-serif;color:var(--text);background:var(--white)}
.abs{position:absolute}
h1,h2,h3{font-family:"Barlow",sans-serif;font-weight:700;color:var(--ink);text-transform:uppercase}

/* header + hero */
.hero{left:0;top:0;width:1200px;height:600px;background:radial-gradient(ellipse at 1130px 280px,#e8401f 0,#7a1d10 60px,transparent 190px),radial-gradient(ellipse at 120px 300px,#5a4634 0,#2a211a 230px,#0b0b0b 430px),#0b0b0b}
.topbar{left:110px;top:13px;font-size:13px;color:#fff;display:flex;gap:16px;align-items:center}
.topbar svg{vertical-align:-2px;margin-right:6px}
.rule{height:1px;background:rgba(255,255,255,.4);top:46px}
.nav{top:61px;display:flex;gap:26px;font-family:"Barlow",sans-serif;font-weight:600;font-size:13.5px;color:#fff;text-transform:uppercase}
.nav .on{border-bottom:2px solid #fff;padding-bottom:6px}
.logo{display:flex;align-items:center;gap:8px;font-family:"Barlow",sans-serif;font-weight:700;font-size:27px}
.logo .dot{width:34px;height:34px;border-radius:50%;background:var(--red)}
.socials{display:flex;gap:5px}
.socials span{width:24px;height:24px;border-radius:50%;border:1.5px solid #fff}
.socials span:first-child{background:var(--red);border-color:var(--red)}
.hero-title{left:368px;top:250px;font-size:36px;color:#fff;letter-spacing:.2px}
.hero-lead{left:370px;top:305px;width:470px;font-size:19.5px;line-height:30px;color:#fff}
.btn{background:var(--red);color:#fff;border-radius:26px;font-family:"Barlow",sans-serif;font-weight:700;font-size:14.5px;display:flex;align-items:center;justify-content:center;text-transform:uppercase}
.arrow{top:272px;width:30px;height:52px;background:#fff}
.arrow.l{left:0;clip-path:polygon(0 0,100% 50%,0 100%)}
.arrow.r{right:0;clip-path:polygon(100% 0,0 50%,100% 100%)}

/* games */
.section-title{left:0;width:1200px;text-align:center;font-size:38px}
.card{top:738px;width:195px;height:236px;background:#fff;box-shadow:0 2px 8px rgba(0,0,0,.15)}
.card .pic{position:absolute;left:6px;top:6px;width:183px;height:176px}
.card b{position:absolute;left:0;right:0;top:198px;text-align:center;color:var(--red);font-weight:600;font-size:17px}

/* charts */
.charts{left:0;top:1041px;width:1200px;height:514px;background:var(--grey-bg)}
.charts h2{left:111px;top:131px;font-size:28px}
.charts .copy{left:111px;top:192px;width:455px;font-size:15px;line-height:25px;color:#666;text-align:justify}
.charts .copy p+p{margin-top:12px}
.window{left:622px;top:100px;width:466px;height:318px;background:#fff;box-shadow:0 4px 14px rgba(0,0,0,.15)}

/* picks */
.picks{left:0;top:1555px;width:1200px;height:400px;background:linear-gradient(100deg,#e84848,#f05757 55%,#e24646)}
.picks h2{left:599px;top:100px;font-size:38px;color:#fff}
.picks p{left:600px;top:170px;width:490px;font-size:14.5px;line-height:25px;color:#fff;text-align:justify}
.laptop{left:113px;top:54px;width:412px;height:268px;background:#e9e9ec;border-radius:12px 12px 0 0;padding:12px}
.laptop-base{left:66px;top:322px;width:506px;height:10px;background:linear-gradient(#f1f1f3,#c7c7cc);border-radius:0 0 50% 50%}

/* winnings */
.winnings-intro{left:160px;top:2125px;width:880px;text-align:center;font-size:15px;line-height:25px;color:#666}
.prize-table{left:201px;top:2212px;width:797px;border-collapse:collapse;font-size:15px;color:#666;text-align:center}
.prize-table th{background:var(--orange);color:#fff;font-family:"Barlow",sans-serif;font-weight:600;font-size:17px;height:50px;border:1px solid #f6b860}
.prize-table td{height:50px;border:1px solid var(--line)}
.prize-table .shade{background:var(--mint)}

/* trial */
.trial{left:0;top:2613px;width:1200px;height:359px;background:radial-gradient(ellipse at 520px 260px,#6b4a30 0,#3a2618 200px,#21150d 480px),#21150d}
.trial h2{left:0;width:1200px;top:58px;text-align:center;font-size:34px;color:#fff}
.trial p{left:148px;top:130px;width:904px;text-align:center;font-size:14.5px;line-height:26px;color:#fff}

/* footer */
.foot-nav{top:3128px;left:0;width:1200px;display:flex;justify-content:center;gap:30px;font-family:"Barlow",sans-serif;font-weight:600;font-size:16.5px;color:var(--ink);text-transform:uppercase}
.foot-contact{top:3168px;left:0;width:1200px;display:flex;justify-content:center;gap:20px;font-size:17px;color:#555}
.foot-contact svg{vertical-align:-2px;margin-right:10px}
.foot-social{top:3213px;left:517px;display:flex;gap:6px}
.foot-social span{width:37px;height:37px;border-radius:50%;border:1.5px solid #222}
.foot-social span:first-child{background:var(--red);border-color:var(--red)}
.foot-rule{left:111px;top:3278px;width:978px;height:1px;background:#333}
.copyright{left:0;width:1200px;top:3298px;text-align:center;font-size:13px;color:#222}
</style>
</head>
<body>

<!-- hero -->
<section class="abs hero" role="img" aria-label="Close-up photo of a dartboard with a red dart flying in from the right"></section>
<div class="abs topbar">
  <span><svg width="12" height="12" viewBox="0 0 24 24" fill="#f03a2b"><path d="M6.6 10.8a15 15 0 0 0 6.6 6.6l2.2-2.2a1 1 0 0 1 1-.25 11.4 11.4 0 0 0 3.6.6 1 1 0 0 1 1 1V20a1 1 0 0 1-1 1A17 17 0 0 1 3 4a1 1 0 0 1 1-1h3.5a1 1 0 0 1 1 1c0 1.25.2 2.45.6 3.6a1 1 0 0 1-.25 1z"/></svg>+1 (555) 014 2290</span>
  <span>|</span>
  <span><svg width="13" height="11" viewBox="0 0 24 18" fill="#f03a2b"><path d="M0 0h24v18H0zM2 2v1l10 7 10-7V2z"/></svg>info@fernwick.com</span>
</div>
<div class="abs rule" style="left:110px;width:362px"></div>
<div class="abs rule" style="left:728px;width:362px"></div>
<nav class="abs nav" style="left:110px"><span class="on">Home</span><span>Latest Drwings</span><span>Create Tickets</span></nav>
<nav class="abs nav" style="left:841px"><span>Statistics &amp; Analysis</span><span>Contact</span></nav>
<div class="abs logo" style="left:498px;top:28px;color:#fff"><span class="dot"></span>Fernwick Lottery</div>
<div class="abs socials" style="left:980px;top:10px"><span></span><span></span><span></span><span></span></div>
<h1 class="abs hero-title">Fernwick Lottery Software</h1>
<p class="abs hero-lead">We use historical lottery data to analyze hot and cold lottery numbers.</p>
<div class="abs btn" style="left:370px;top:388px;width:146px;height:50px">Get Started</div>
<div class="abs arrow l"></div>
<div class="abs arrow r"></div>

<!-- games -->
<h2 class="abs section-title" style="top:658px">All Major Lottery Games</h2>
<div class="abs card" style="left:82px"><div class="pic" role="img" aria-label="Darts with flag flights in a dartboard" style="background:linear-gradient(135deg,#d6d9cf,#c8867c 55%,#e9e3da)"></div><b>United States</b></div>
<div class="abs card" style="left:293px"><div class="pic" role="img" aria-label="City skyline with a tall tower under blue sky" style="background:linear-gradient(#3b8fd8,#8ec3ee 55%,#5a7c8a)"></div><b>Canada</b></div>
<div class="abs card" style="left:503px"><div class="pic" role="img" aria-label="Historic European castle at sunset" style="background:linear-gradient(#c9b7a0,#9a6a3c 55%,#4d3a28)"></div><b>Europe</b></div>
<div class="abs card" style="left:714px"><div class="pic" role="img" aria-label="Dartboard with a dart near the centre" style="background:linear-gradient(160deg,#2a3a36,#1a1d1c 60%,#2c2a26)"></div><b>United Kingdom</b></div>
<div class="abs card" style="left:924px"><div class="pic" role="img" aria-label="Target board hanging on a dark brick wall" style="background:linear-gradient(160deg,#4a4a4a,#2a2a2a 60%,#1d1d1d)"></div><b>Coming Soon</b></div>

<!-- charts -->
<section class="abs charts">
  <h2 class="abs">Charts and Analysis</h2>
  <div class="abs copy">
    <p>Lorem ipsum dolor sit amet, consectetur adipiscing elit, sed do eiusmod tempor incididunt ut labore et dolore magna aliqua. Ut enim ad minim veniam, quis nostrud exercitation ullamco laboris nisi ut aliquip ex ea commodo consequat.</p>
    <p>Tempor incididunt ut labore et dolore magna aliqua. Ut enim ad minim veniam, quis nostrud exercitation ullamco laboris nisi ut aliquip ex ea commodo consequat.</p>
  </div>
  <div class="abs window">
    <svg width="466" height="318" viewBox="0 0 466 318">
      <circle cx="28" cy="11" r="3.5" fill="#f0522b"/><circle cx="37" cy="11" r="3.5" fill="#f5a623"/><circle cx="46" cy="11" r="3.5" fill="#2b9d4a"/>
      <rect x="10" y="20" width="446" height="8" fill="#f0f0f0"/>
      <rect x="10" y="28" width="446" height="282" fill="#ececec"/>
      <rect x="10" y="28" width="74" height="282" fill="#f4f4f4"/>
      <line x1="84" y1="28" x2="84" y2="310" stroke="#666"/>
      <rect x="18" y="52" width="56" height="10" fill="#d5e2f4"/>
      <rect x="18" y="94" width="56" height="8" fill="#fff" stroke="#aaa" stroke-width=".5"/>
      <rect x="18" y="134" width="56" height="8" fill="#fff" stroke="#4a7fd0" stroke-width=".5"/>
      <text x="265" y="50" font-size="7" fill="#555" text-anchor="middle" font-family="Work Sans,sans-serif">Number Frequency Chart</text>
      <rect x="104" y="58" width="340" height="220" fill="#fff"/>
      <g stroke="#eee">
        <line x1="104" y1="80" x2="444" y2="80"/><line x1="104" y1="120" x2="444" y2="120"/><line x1="104" y1="160" x2="444" y2="160"/><line x1="104" y1="200" x2="444" y2="200"/><line x1="104" y1="240" x2="444" y2="240"/>
      </g>
      <g fill="#f07a4a">
        <rect x="110" y="210" width="2" height="68"/><rect x="118" y="230" width="2" height="48"/><rect x="126" y="180" width="2" height="98"/><rect x="134" y="150" width="2" height="128"/><rect x="142" y="220" width="2" height="58"/><rect x="150" y="190" width="2" height="88"/><rect x="158" y="240" width="2" height="38"/><rect x="166" y="200" width="2" height="78"/><rect x="174" y="225" width="2" height="53"/><rect x="182" y="170" width="2" height="108"/><rect x="190" y="210" width="2" height="68"/><rect x="198" y="245" width="2" height="33"/><rect x="206" y="195" width="2" height="83"/><rect x="214" y="230" width="2" height="48"/><rect x="222" y="205" width="2" height="73"/><rect x="230" y="175" width="2" height="103"/><rect x="238" y="235" width="2" height="43"/><rect x="246" y="200" width="2" height="78"/><rect x="254" y="215" width="2" height="63"/><rect x="262" y="225" width="2" height="53"/><rect x="270" y="78" width="2" height="200"/><rect x="278" y="210" width="2" height="68"/><rect x="286" y="240" width="2" height="38"/><rect x="294" y="195" width="2" height="83"/><rect x="302" y="220" width="2" height="58"/><rect x="310" y="185" width="2" height="93"/><rect x="318" y="230" width="2" height="48"/><rect x="326" y="205" width="2" height="73"/><rect x="334" y="245" width="2" height="33"/><rect x="342" y="215" width="2" height="63"/><rect x="350" y="190" width="2" height="88"/><rect x="358" y="225" width="2" height="53"/><rect x="366" y="200" width="2" height="78"/><rect x="374" y="235" width="2" height="43"/><rect x="382" y="210" width="2" height="68"/><rect x="390" y="138" width="2" height="140"/><rect x="398" y="220" width="2" height="58"/><rect x="406" y="195" width="2" height="83"/><rect x="414" y="240" width="2" height="38"/><rect x="422" y="215" width="2" height="63"/><rect x="430" y="230" width="2" height="48"/>
      </g>
      <rect x="252" y="294" width="5" height="4" fill="#f07a4a"/>
    </svg>
  </div>
</section>

<!-- picks -->
<section class="abs picks">
  <div class="abs laptop">
    <svg width="388" height="244" viewBox="0 0 388 244">
      <rect width="388" height="244" fill="#fff"/>
      <rect x="6" y="6" width="40" height="226" fill="#9a9a9a"/>
      <text x="200" y="30" font-size="8.5" fill="#222" text-anchor="middle" font-family="Work Sans,sans-serif" font-weight="600">Create Smart Number Tickets</text>
      <rect x="70" y="40" width="250" height="22" fill="none" stroke="#bbb" stroke-width=".6"/>
      <rect x="70" y="68" width="250" height="124" fill="none" stroke="#bbb" stroke-width=".6"/>
      <rect x="71" y="72" width="248" height="5" fill="#3a7bd5"/>
      <g fill="#888"><rect x="74" y="82" width="110" height="2"/><rect x="74" y="89" width="110" height="2"/><rect x="74" y="96" width="110" height="2"/><rect x="74" y="103" width="110" height="2"/><rect x="74" y="110" width="110" height="2"/><rect x="74" y="117" width="110" height="2"/><rect x="74" y="124" width="110" height="2"/><rect x="74" y="131" width="110" height="2"/><rect x="74" y="138" width="110" height="2"/><rect x="74" y="145" width="110" height="2"/><rect x="74" y="152" width="110" height="2"/><rect x="74" y="159" width="110" height="2"/></g>
      <rect x="330" y="68" width="40" height="10" fill="#eee" stroke="#aaa" stroke-width=".5"/>
      <rect x="330" y="86" width="40" height="10" fill="#eee" stroke="#aaa" stroke-width=".5"/>
      <line x1="0" y1="232" x2="388" y2="232" stroke="#ccc"/>
    </svg>
  </div>
  <div class="abs laptop-base"></div>
  <h2 class="abs">Fernwick Picks</h2>
  <p class="abs">Sed ut perspiciatis unde omnis iste natus error sit voluptatem accusantium doloremque laudantium, totam rem aperiam, eaque ipsa quae ab illo inventore veritatis et quasi architecto beatae vitae dicta sunt explicabo. Nemo enim ipsam voluptatem quia voluptas sit aspernatur aut odit aut fia consequuntur.</p>
</section>

<!-- winnings -->
<h2 class="abs section-title" style="top:2062px">Track Your Winnings</h2>
<p class="abs winnings-intro">At vero eos et accusamus et iusto odio dignissimos ducimus qui blanditiis praesentium voluptatum deleniti atque corrupti quos dolores et quas molestias excepturi sint occaecati.</p>
<table class="abs prize-table">
  <tr><th style="width:244px">DIVISION</th><th style="width:258px">PRIZES</th><th>WINNERS</th></tr>
  <tr><td class="shade">1</td><td>$1000</td><td class="shade">Lorum Ipsum Dol</td></tr>
  <tr><td>2</td><td class="shade">$1000</td><td>Lorum Ipsum Dol</td></tr>
  <tr><td class="shade">3</td><td>$1000</td><td class="shade">Lorum Ipsum Dol</td></tr>
  <tr><td>4</td><td class="shade">$1000</td><td>Lorum Ipsum Dol</td></tr>
  <tr><td class="shade">5</td><td>$1000</td><td class="shade">Lorum Ipsum Dol</td></tr>
</table>

<!-- trial -->
<section class="abs trial" role="img" aria-label="Dark photo of a dart striking a dartboard">
  <h2 class="abs">14 Day Free Trial</h2>
  <p class="abs">At vero eos et accusamus et iusto odio dignissimos ducimus qui blanditiis praesentium voluptatum deleniti atque corrupti quos dolores et quas molestias excepturi sint occaecati cupiditate non provident, similique sunt in culpa qui officia deserunt mollitia animi, id est laborum et dolorerum facilis est et expedita distinctio.</p>
  <div class="abs btn" style="left:533px;top:242px;width:134px;height:50px">Join Now</div>
</section>

<!-- footer -->
<div class="abs logo" style="left:488px;top:3055px;color:var(--ink);font-size:30px"><span class="dot" style="width:38px;height:38px"></span>Fernwick Lottery</div>
<nav class="abs foot-nav"><span>Home</span><span>Latest Drwings</span><span>Create Tickets</span><span>Statistics &amp; Analysis</span><span>Contact</span></nav>
<div class="abs foot-contact">
  <span><svg width="14" height="14" viewBox="0 0 24 24" fill="#f03a2b"><path d="M6.6 10.8a15 15 0 0 0 6.6 6.6l2.2-2.2a1 1 0 0 1 1-.25 11.4 11.4 0 0 0 3.6.6 1 1 0 0 1 1 1V20a1 1 0 0 1-1 1A17 17 0 0 1 3 4a1 1 0 0 1 1-1h3.5a1 1 0 0 1 1 1c0 1.25.2 2.45.6 3.6a1 1 0 0 1-.25 1z"/></svg>+1 (555) 014 2290</span>
  <span>|</span>
  <span><svg width="17" height="13" viewBox="0 0 24 18" fill="#f03a2b"><path d="M0 0h24v18H0zM2 2v1l10 7 10-7V2z"/></svg>info@fernwick.com</span>
</div>
<div class="abs foot-social"><span></span><span></span><span></span><span></span></div>
<div class="abs foot-rule"></div>
<p class="abs copyright">© 2022 Fernwick Lottery Software. All Rights Reserved</p>

</body>
</html>
```